Web Design Project

The Varnholt Group is a strategy consulting group that works primarily with the healthcare industry. We provide a limited range of strategic planning & marketing services designed to focus on the growth and future viability of our clients’ organizations. We are a very small organization, but want to communicate a sense of boldness, forward-looking/visionary, and both creative and analytic. What follows below is: 1) A simple overview of the outline of the web-pages; 2) an important list of web-sites that appeal to me – the most important of which appears in a larger font; 3) photo ideas for the home page (from Pixwellone.com). I have not written copy…and won’t until I know length based upon design.

The Varnholt Group
Healthcare Strategic Consulting

(Key Sections for the site)
HOME PAGE ABOUT US SERVICES NEWS & COMMENTS CONTACT US

(Sites That I Admire:)

http://www.brimandtusk.eu/services/ Very creative use of iconography to represent services, etc.

http://quietcomber.com/ Arresting graphics

http://plumtrace.co/ GREAT SITE. THIS IS THE SITE THAT I LIKE THE MOST IN TERMS OF GENERAL LOOK & FEEL.

http://korvagroup.com/ Very interesting, stark/bold B&W site for architects

http://www.pmfarrow.com/ Interesting home page for promoting individual

HOME PAGE:

The Varnholt Group
STRATEGIC CONSULTING SERVICES (should be bold). We have a Logo that can be supplied later

Pixwell Image Options: 47195362, 63804152, 29736481, 58241607, 274618530, 16490823
Updates

Project Deadline Extended
Reason: The 1st and 2nd place designers will have an additional 5-7 days to complete the remaining pages of the site (approximately 11 pages). I have a file with all the photo information and rough copy that can be dropped into position.

Target Market(s)

Senior Executives (CEO,COO, CFO,SVP) in major hospitals or healthcare systems, other senior executives within healthcare.

Industry/Entity Type

Healthcare

Requirements
Must have
• I will want to pay to have this project expanded to show look and feel for:
*Home Page and key sections
*4 Pages that will be under the "About Us" heading
*5 Pages that will be under the "Services" heading

I have image options selected from Pixwell for all key sections. We will need to look at the cost for those images that the designer recommends.

```html
<!DOCTYPE html>
<html lang="en">
<head>
<meta charset="utf-8">
<title>Contact Us – The Varnholt Group</title>
<link href="https://fonts.googleapis.com/css2?family=Marcellus&family=PT+Sans:ital,wght@0,400;0,700;1,400&family=PT+Sans+Narrow:wght@400;700&display=swap" rel="stylesheet">
<style>
  :root {
    --header-dark: #27313b;
    --header-mid: #4f5e6c;
    --header-light: #8c97a1;
    --heading-grey: #8a9697;
    --label-grey: #8d8d8d;
    --text-grey: #666a6c;
    --field-bg: #f0f0f0;
    --button-bg: #7b7b7b;
    --rule: #e6e6e6;
    --white: #ffffff;
    --map-bg: #e6e2d8;
    --map-frame: #e9e9e9;
    --dark-circle: #3f3f3f;
    --icon-grey: #b4b4b4;
    --social-grey: #6e6e6e;
  }
  * { box-sizing: border-box; margin: 0; padding: 0; }
  html, body { width: 1200px; height: 1186px; overflow: hidden; background: var(--white); }
  body { position: relative; font-family: "PT Sans", sans-serif; color: var(--text-grey); }
  .abs { position: absolute; }

  .site-header {
    position: absolute; left: 0; top: 0; width: 1200px; height: 128px;
    background: linear-gradient(100deg, var(--header-dark) 0%, var(--header-mid) 35%, var(--header-light) 60%, var(--header-mid) 85%, var(--header-dark) 100%);
  }
  .brand-name {
    left: 90px; top: 22px; font-family: "Marcellus", serif; font-size: 50px;
    color: var(--white); line-height: 1; white-space: nowrap;
  }
  .brand-rule { top: 84px; height: 1px; background: rgba(255,255,255,.6); }
  .brand-tagline { left: 300px; width: 195px; top: 93px; text-align: right; font-size: 13px; color: var(--white); }
  .main-nav { right: 89px; top: 53px; display: flex; font-size: 13px; color: var(--white); text-transform: uppercase; }
  .main-nav span { padding: 0 8px; }
  .main-nav .sep { padding: 0 7px; }
  .main-nav .current { border-bottom: 2px solid var(--white); padding: 0 0 2px; margin: 0 8px; }

  .page-title {
    left: 0; width: 1200px; top: 178px; text-align: center;
    font-family: "PT Sans Narrow", sans-serif; font-weight: 700; font-size: 58px;
    color: var(--heading-grey); line-height: 1;
  }
  .page-intro {
    left: 0; width: 1200px; top: 268px; text-align: center;
    font-family: "PT Sans Narrow", sans-serif; font-weight: 700; font-size: 23px; color: var(--heading-grey);
  }
  .divider { left: 151px; width: 898px; height: 1px; background: linear-gradient(90deg, transparent, var(--rule) 15%, var(--rule) 85%, transparent); }

  .section-title { font-family: "PT Sans Narrow", sans-serif; font-weight: 700; font-size: 23px; color: var(--heading-grey); }

  .field-label { font-size: 12px; font-style: italic; color: var(--label-grey); }
  .field { background: var(--field-bg); border-radius: 3px; }
  .submit-button {
    left: 923px; top: 592px; width: 119px; height: 47px; background: var(--button-bg);
    border-radius: 3px; color: var(--white); font-family: "PT Sans Narrow", sans-serif;
    font-size: 19px; text-align: center; line-height: 47px;
  }

  .map-frame { left: 157px; top: 805px; width: 367px; height: 196px; background: var(--map-frame); padding: 6px; }
  .map-area { width: 100%; height: 100%; background: linear-gradient(135deg, var(--map-bg), #f0ecdf 60%, #ddd8cc); }
  .column-rule { left: 570px; top: 756px; width: 1px; height: 245px; background: #d8d8d8; }
  .arrow-badge { left: 552px; top: 850px; }

  .info-label { font-size: 13px; color: var(--heading-grey); text-transform: uppercase; }
  .info-text { font-size: 12px; line-height: 19px; color: var(--text-grey); }

  .footer-nav { left: 90px; top: 1102px; font-size: 12px; color: var(--text-grey); display: flex; }
  .footer-nav .sep { padding: 0 13px; }
  .copyright { left: 90px; top: 1133px; font-size: 12px; color: var(--text-grey); }
  .social-square { top: 1110px; width: 30px; height: 30px; background: var(--social-grey); border-radius: 3px; }
</style>
</head>
<body>
  <header class="site-header" role="img" aria-label="Photograph of yellow road signs with upward arrows under an evening sky">
  </header>
  <div class="abs brand-name">The Varnholt Group</div>
  <div class="abs brand-rule" style="left:90px;width:369px;"></div>
  <div class="abs brand-rule" style="left:480px;width:631px;"></div>
  <div class="abs brand-tagline">Healthcare Strategic Consulting</div>
  <nav class="abs main-nav">
    <span class="current">Home</span><span class="sep">|</span>
    <span>About us</span><span class="sep">|</span>
    <span>Services</span><span class="sep">|</span>
    <span>News &amp; Comments</span><span class="sep">|</span>
    <span style="padding-right:0">Contact us</span>
  </nav>

  <h1 class="abs page-title">CONTACT US</h1>
  <p class="abs page-intro">Excepteur sint occaecat cupidatat non proident sunt inculpa le officia</p>
  <div class="abs divider" style="top:341px"></div>

  <h2 class="abs section-title" style="left:157px;top:382px">Send us a Message</h2>
  <div class="abs field-label" style="left:157px;top:459px">Name :</div>
  <div class="abs field" style="left:246px;top:443px;width:307px;height:46px"></div>
  <div class="abs field-label" style="left:157px;top:533px">Phone :</div>
  <div class="abs field" style="left:246px;top:517px;width:307px;height:46px"></div>
  <div class="abs field-label" style="left:157px;top:607px">E-mail :</div>
  <div class="abs field" style="left:246px;top:592px;width:307px;height:46px"></div>
  <div class="abs field-label" style="left:595px;top:459px">Message :</div>
  <div class="abs field" style="left:684px;top:443px;width:358px;height:121px"></div>
  <div class="abs submit-button">SUBMIT</div>
  <div class="abs divider" style="top:707px"></div>

  <h2 class="abs section-title" style="left:157px;top:752px">Contact us</h2>
  <div class="abs map-frame"><div class="map-area" role="img" aria-label="Street map showing the office location"></div></div>
  <div class="abs column-rule"></div>
  <svg class="abs arrow-badge" width="37" height="37" viewBox="0 0 37 37" aria-hidden="true">
    <circle cx="18.5" cy="18.5" r="18.5" fill="var(--dark-circle)"/>
    <path d="M11 18.5h12M18 13l5.5 5.5L18 24" stroke="#fff" stroke-width="3" fill="none" stroke-linecap="round" stroke-linejoin="round"/>
  </svg>

  <div class="abs info-label" style="left:608px;top:798px">Address</div>
  <div class="abs info-text" style="left:608px;top:825px">Curabitur mollis varius massa<br>eget commodo neque<br>City Name</div>

  <svg class="abs" style="left:608px;top:908px" width="26" height="20" viewBox="0 0 26 20" aria-hidden="true">
    <path d="M3 2c-2 2-1 6 3 10s8 6 10 4l2-2-4-3-2 2c-2-1-4-3-5-5l2-2-3-4z" fill="var(--icon-grey)"/>
    <path d="M18 6a4 4 0 0 1 3 3M19 3a7 7 0 0 1 5 5" stroke="var(--icon-grey)" stroke-width="1.5" fill="none"/>
  </svg>
  <svg class="abs" style="left:766px;top:908px" width="22" height="20" viewBox="0 0 22 20" aria-hidden="true">
    <rect x="5" y="1" width="12" height="5" fill="var(--icon-grey)"/>
    <rect x="1" y="6" width="20" height="9" rx="2" fill="var(--icon-grey)"/>
    <rect x="5" y="12" width="12" height="7" fill="#fff" stroke="var(--icon-grey)" stroke-width="2"/>
  </svg>
  <svg class="abs" style="left:913px;top:908px" width="24" height="20" viewBox="0 0 24 20" aria-hidden="true">
    <path d="M2 9l10-7 10 7v10H2z" fill="var(--icon-grey)"/>
    <path d="M2 9l10 6 10-6" stroke="#fff" stroke-width="1.5" fill="none"/>
  </svg>

  <div class="abs info-label" style="left:609px;top:942px">Phone</div>
  <div class="abs info-text" style="left:608px;top:968px">318 402 7715<br>318 402 7790</div>
  <div class="abs info-label" style="left:767px;top:942px">Fax</div>
  <div class="abs info-text" style="left:766px;top:968px">318 402 7762</div>
  <div class="abs info-label" style="left:914px;top:942px">Email</div>
  <div class="abs info-text" style="left:913px;top:968px">info@thevarnholt.com</div>

  <div class="abs divider" style="top:1063px"></div>
  <nav class="abs footer-nav">
    <span>Home</span><span class="sep">|</span>
    <span>About us</span><span class="sep">|</span>
    <span>Services</span><span class="sep">|</span>
    <span>News &amp; Comments</span><span class="sep">|</span>
    <span>Contact us</span>
  </nav>
  <div class="abs copyright">Copyright © 2012 www.thevarnholt.com &nbsp; All rights reserved.</div>
  <div class="abs social-square" style="left:995px" aria-label="Social link"></div>
  <div class="abs social-square" style="left:1039px" aria-label="Social link"></div>
  <div class="abs social-square" style="left:1082px" aria-label="Social link"></div>
</body>
</html>
```